New Business and Accounting Software need a Web Site

The website is for a Business and Accounting Software that has 8 products.
Each product has its owns logo and color, when you do the design have in consideration that we are looking the experience that when you change from one product page to another the look and feel adjust to the color and logo of the product.
The product are:
Ventas (Sales)
Compras (Purchases)
Contabilidad (Accounting)
Presupuesto (Budget)
Inventarios (Inventory)
Bancos (Banks)
NĂ³mina RH (Human Resources Payroll)
CRM (Customer Relationship Manager)

You can see how the main logo and variations are used in each page
- https://www.ufta.com/
- https://www.vemi.com/
- https://www.prulvin.com/

Our goal is to be similar to them.

I have created a word document to explain what I want.
You need to design:
1 Home Page
1 Product Landing Page
1 Product Detail Page
1 Price Page

I am attaching:
1. Main Logo
2. 8 Product Logos
3. Website Idea, you can create your own idea.

You are welcome to use other icons for the each product if you want.

Target Market(s)

Independet professionals and Small and Medium Companies

Industry/Entity Type

Business and Accounting Software

Coding

Coded - Design and coding required

Colors
0054AA
0677BA
7BADD7
CADEEF
E8F1F8

Requirements
Must have
• Must show all products in the main page

```html
<!DOCTYPE html>
<html lang="en">
<head>
<meta charset="utf-8">
<title>Velto.cr — Business and Accounting Software</title>
<link href="https://fonts.googleapis.com/css2?family=Poppins:wght@400;500;600;700;800&family=Roboto:wght@400;500;700&display=swap" rel="stylesheet">
<style>
:root{
  --blue:#0054AA;
  --blue-2:#0677BA;
  --blue-3:#7BADD7;
  --blue-4:#CADEEF;
  --blue-5:#E8F1F8;
  --orange:#FDB53A;
  --white:#ffffff;
  --ink:#1c2430;
  --ventas:#FDB53A;--compras:#87C7F7;--conta:#C86FD8;--presu:#26C896;
  --inv:#DE5868;--bancos:#9D9D9D;--nomina:#65B7C1;--crm:#7577DB;
}
*{margin:0;padding:0;box-sizing:border-box}
html,body{width:1200px;height:3680px;overflow:hidden}
body{position:relative;background:#fff;font-family:"Roboto",sans-serif;color:var(--ink)}
.abs{position:absolute}
/* header */
.site-header{position:absolute;top:0;left:0;width:1200px;height:93px;background:#fff;border-top:4px solid var(--blue);z-index:5}
.brand{position:absolute;left:111px;top:22px;display:flex;align-items:center;gap:10px;font-family:"Poppins",sans-serif;font-weight:700;font-size:40px;color:var(--blue);line-height:1}
.brand-dot{width:40px;height:40px;border-radius:50%;background:var(--blue)}
.nav{position:absolute;left:478px;top:38px;display:flex;gap:30px;font-weight:700;font-size:14px;color:var(--blue)}
.nav a{color:inherit;text-decoration:none}
.nav .active{border-bottom:3px solid var(--blue);padding-bottom:4px}
.btn-outline{position:absolute;height:42px;border-radius:21px;border:2px solid var(--blue);font-weight:700;font-size:14px;color:var(--blue);display:flex;align-items:center;justify-content:center;gap:6px}
.signin{left:836px;top:26px;width:106px}
.trial-top{left:956px;top:26px;width:133px;border-color:var(--blue-3);color:var(--blue-3)}
/* hero */
.hero-photo{position:absolute;left:0;top:93px;width:1200px;height:720px;background:linear-gradient(100deg,#eef3f7 0%,#dfe6ec 35%,#b9a896 60%,#8c9aa8 100%)}
.hero-circle{position:absolute;left:10px;top:190px;width:400px;height:400px;border-radius:50%;background:rgba(202,222,239,.55)}
.hero-title{position:absolute;left:108px;top:264px;font-family:"Poppins",sans-serif;font-weight:800;font-size:70px;color:var(--blue);line-height:1}
.hero-text{position:absolute;left:111px;top:356px;width:360px;font-family:"Poppins",sans-serif;font-size:14.5px;line-height:26px;color:#333}
.hero-btn{left:111px;top:430px;width:134px;height:42px;background:#fff}
.dots{position:absolute;left:112px;top:581px;display:flex;gap:6px}
.dots i{width:14px;height:14px;border-radius:50%;border:2px solid var(--blue);display:block}
.dots i.on{background:var(--blue)}
/* products */
.section-title{position:absolute;left:0;width:1200px;text-align:center;font-family:"Poppins",sans-serif;font-weight:700;font-size:44px;color:var(--blue)}
.title-rule{position:absolute;left:562px;width:76px;height:4px;background:var(--blue)}
.card{position:absolute;width:235px;height:286px;padding:24px 29px;color:#fff}
.card svg.icon{width:62px;height:56px;display:block}
.card h3{font-family:"Poppins",sans-serif;font-weight:600;font-size:19px;margin-top:12px}
.card .dash{width:20px;height:2px;background:#fff;margin:10px 0 16px}
.card p{font-size:12.5px;line-height:26px;opacity:.95}
.card .go{position:absolute;left:29px;bottom:22px;width:22px;height:22px;border-radius:50%;background:rgba(0,0,0,.25)}
.card .go svg{position:absolute;left:5px;top:4px}
/* product tabs */
.tabs{position:absolute;left:279px;top:1933px;display:flex;gap:14px}
.tab{position:relative;height:46px;padding:0 20px;background:#fff;font-family:"Poppins",sans-serif;font-weight:600;font-size:19px;color:var(--ink);display:flex;align-items:center}
.tab.on{background:var(--orange);color:#fff}
.tab.on:after{content:"";position:absolute;left:50%;bottom:-14px;margin-left:-9px;border:9px solid transparent;border-top:14px solid var(--orange);border-bottom:0}
.p-title{position:absolute;left:111px;top:2050px;font-family:"Poppins",sans-serif;font-weight:700;font-size:34px;color:#fff}
.p-text{position:absolute;left:111px;top:2112px;width:484px;font-size:15px;line-height:25.7px;color:#fff;text-align:justify}
.laptop{position:absolute;left:598px;top:2057px;width:540px;height:313px;border-radius:10px;background:linear-gradient(180deg,#f4f7fa,#dfe6ee)}
/* cta */
.cta-box{position:absolute;left:111px;top:2550px;width:384px;height:453px;border-radius:40px;background:var(--blue)}
.cta-person{position:absolute;left:179px;top:2497px;width:361px;height:506px;background:linear-gradient(180deg,#d7c6b5 0%,#6f7d5c 40%,#5a6a4c 100%);border-radius:90px 90px 0 0;opacity:.9}
.cta-head{position:absolute;left:600px;top:2663px;width:520px;font-family:"Poppins",sans-serif;font-weight:700;font-size:44px;line-height:52px;color:var(--blue)}
.cta-head span{color:var(--orange)}
.cta-btn{left:601px;top:2838px;width:227px;height:42px;font-size:13.5px}
/* footer */
.footer-col{position:absolute;top:3368px;color:#fff}
.footer-col h4{font-family:"Poppins",sans-serif;font-weight:700;font-size:21px;letter-spacing:.5px;margin-bottom:14px}
.footer-col li{list-style:none;font-size:14.5px;line-height:30.5px}
.contact-row{display:flex;gap:20px;font-size:14.5px;line-height:25px;margin-bottom:18px}
.contact-row svg{flex:none;margin-top:6px}
.foot-brand{position:absolute;left:860px;top:3360px;display:flex;align-items:center;gap:12px;font-family:"Poppins",sans-serif;font-weight:700;font-size:46px;color:#fff;line-height:1}
.foot-brand i{width:56px;height:56px;border-radius:50%;background:#fff;display:block}
.slogan{position:absolute;left:870px;top:3500px;font-family:"Poppins",sans-serif;font-size:16px;color:#fff}
.socials{position:absolute;left:870px;top:3532px;display:flex;gap:12px}
.socials i{width:10px;height:10px;border-radius:50%;background:var(--blue-3);display:block}
.copyright{position:absolute;left:0;top:3620px;width:1200px;text-align:center;font-family:"Poppins",sans-serif;font-size:13.5px;color:#fff}
</style>
</head>
<body>

<header class="site-header">
  <div class="brand"><span class="brand-dot"></span>velto.cr</div>
  <nav class="nav">
    <a class="active">HOME</a><a>SOLUTIONS</a><a>PLANS</a><a>CONTACT</a>
  </nav>
  <div class="btn-outline signin">SIGNIN</div>
  <div class="btn-outline trial-top">FREE TRIAL</div>
</header>

<!-- hero -->
<div class="hero-photo" role="img" aria-label="Photo of three young professionals smiling while working at computers in a bright office"></div>
<div class="hero-circle"></div>
<svg class="abs" style="left:0;top:620px" width="1200" height="240" viewBox="0 0 1200 240">
  <polygon points="0,80 307,234 1071,37 1200,25 1200,240 0,240" fill="#fff"/>
  <polygon points="0,9 307,173 1071,37 307,234 0,80" fill="var(--blue)"/>
  <polyline points="0,51 307,173 1071,37" fill="none" stroke="#fff" stroke-width="3"/>
</svg>
<h1 class="hero-title">VELTO</h1>
<p class="hero-text">Lorem ipsum dolor sit amet, consectetur adip iscing elit, sed do eiusmod tempor</p>
<div class="btn-outline hero-btn">FREE TRIAL</div>
<div class="dots"><i class="on"></i><i></i><i></i></div>

<!-- products -->
<h2 class="section-title" style="top:930px">Our Product</h2>
<div class="title-rule" style="top:996px"></div>

<div class="card" style="left:111px;top:1028px;background:var(--ventas)">
  <svg class="icon" viewBox="0 0 62 56"><rect x="2" y="40" width="7" height="14" fill="#fff"/><rect x="13" y="32" width="7" height="22" fill="#fff"/><rect x="24" y="24" width="7" height="30" fill="#fff"/><rect x="35" y="16" width="7" height="38" fill="#fff"/><path d="M4 30 L40 4" stroke="#fff" stroke-width="3"/><path d="M32 3 L42 3 L41 13" fill="none" stroke="#fff" stroke-width="3"/></svg>
  <h3>Ventas</h3><div class="dash"></div>
  <p>Lorem ipsum dolor sit amet, consectetur adipiscing elit, s ed do eiusmod tempor</p>
  <span class="go"><svg width="14" height="14" viewBox="0 0 14 14"><path d="M1 7h11M8 3l4 4-4 4" stroke="#fff" stroke-width="1.6" fill="none"/></svg></span>
</div>
<div class="card" style="left:358px;top:1028px;background:var(--compras)">
  <svg class="icon" viewBox="0 0 62 56"><path d="M8 22h46l-4 32H12z" fill="#fff"/><path d="M20 22a11 11 0 0 1 22 0" fill="none" stroke="#fff" stroke-width="3"/><rect x="2" y="14" width="30" height="4" fill="#fff"/></svg>
  <h3>Compras</h3><div class="dash"></div>
  <p>Lorem ipsum dolor sit amet, consectetur adipiscing elit, s ed do eiusmod tempor</p>
  <span class="go"><svg width="14" height="14" viewBox="0 0 14 14"><path d="M1 7h11M8 3l4 4-4 4" stroke="#fff" stroke-width="1.6" fill="none"/></svg></span>
</div>
<div class="card" style="left:606px;top:1028px;background:var(--conta)">
  <svg class="icon" viewBox="0 0 62 56"><rect x="2" y="4" width="20" height="20" rx="3" fill="#fff"/><rect x="26" y="4" width="20" height="20" rx="3" fill="#fff"/><rect x="2" y="28" width="20" height="20" rx="3" fill="#fff"/><rect x="26" y="28" width="20" height="20" rx="3" fill="#fff"/><path d="M40 50 Q58 36 56 6" fill="none" stroke="#fff" stroke-width="3"/></svg>
  <h3>Contabilidad</h3><div class="dash"></div>
  <p>Lorem ipsum dolor sit amet, consectetur adipiscing elit, s ed do eiusmod tempor</p>
  <span class="go"><svg width="14" height="14" viewBox="0 0 14 14"><path d="M1 7h11M8 3l4 4-4 4" stroke="#fff" stroke-width="1.6" fill="none"/></svg></span>
</div>
<div class="card" style="left:853px;top:1028px;background:var(--presu)">
  <svg class="icon" viewBox="0 0 62 56"><path d="M4 40a27 27 0 0 1 54 0" fill="none" stroke="#fff" stroke-width="3"/><ellipse cx="31" cy="22" rx="12" ry="5" fill="#fff"/><ellipse cx="20" cy="32" rx="11" ry="5" fill="#fff"/><ellipse cx="42" cy="32" rx="11" ry="5" fill="#fff"/></svg>
  <h3>Presupuesto</h3><div class="dash"></div>
  <p>Lorem ipsum dolor sit amet, consectetur adipiscing elit, s ed do eiusmod tempor</p>
  <span class="go"><svg width="14" height="14" viewBox="0 0 14 14"><path d="M1 7h11M8 3l4 4-4 4" stroke="#fff" stroke-width="1.6" fill="none"/></svg></span>
</div>

<div class="card" style="left:111px;top:1328px;background:var(--inv)">
  <svg class="icon" viewBox="0 0 62 56"><path d="M4 14 L22 6 L40 14 L40 44 L22 52 L4 44z" fill="#fff"/><rect x="42" y="24" width="18" height="28" fill="#fff"/></svg>
  <h3>Inventarios</h3><div class="dash"></div>
  <p>Lorem ipsum dolor sit amet, consectetur adipiscing elit, s ed do eiusmod tempor</p>
  <span class="go"><svg width="14" height="14" viewBox="0 0 14 14"><path d="M1 7h11M8 3l4 4-4 4" stroke="#fff" stroke-width="1.6" fill="none"/></svg></span>
</div>
<div class="card" style="left:358px;top:1328px;background:var(--bancos)">
  <svg class="icon" viewBox="0 0 62 56"><path d="M4 18 L28 4 L52 18z" fill="#fff"/><rect x="6" y="22" width="6" height="24" fill="#fff"/><rect x="44" y="22" width="6" height="24" fill="#fff"/><rect x="16" y="22" width="24" height="24" fill="#fff"/><rect x="2" y="48" width="52" height="6" fill="#fff"/></svg>
  <h3>Bancos</h3><div class="dash"></div>
  <p>Lorem ipsum dolor sit amet, consectetur adipiscing elit, s ed do eiusmod tempor</p>
  <span class="go"><svg width="14" height="14" viewBox="0 0 14 14"><path d="M1 7h11M8 3l4 4-4 4" stroke="#fff" stroke-width="1.6" fill="none"/></svg></span>
</div>
<div class="card" style="left:606px;top:1328px;background:var(--nomina)">
  <svg class="icon" viewBox="0 0 62 56"><path d="M4 40a27 27 0 0 1 54 0" fill="none" stroke="#fff" stroke-width="3"/><circle cx="18" cy="24" r="6" fill="#fff"/><circle cx="44" cy="24" r="6" fill="#fff"/><circle cx="31" cy="18" r="7" fill="#fff"/><rect x="10" y="32" width="16" height="18" rx="4" fill="#fff"/><rect x="36" y="32" width="16" height="18" rx="4" fill="#fff"/><rect x="22" y="28" width="18" height="24" rx="4" fill="#fff"/></svg>
  <h3>Nómina RH</h3><div class="dash"></div>
  <p>Lorem ipsum dolor sit amet, consectetur adipiscing elit, s ed do eiusmod tempor</p>
  <span class="go"><svg width="14" height="14" viewBox="0 0 14 14"><path d="M1 7h11M8 3l4 4-4 4" stroke="#fff" stroke-width="1.6" fill="none"/></svg></span>
</div>
<div class="card" style="left:853px;top:1328px;background:var(--crm)">
  <svg class="icon" viewBox="0 0 62 56"><path d="M4 40a27 27 0 0 1 54 0" fill="none" stroke="#fff" stroke-width="3"/><path d="M6 36 L18 24 L30 30 L42 22 L56 34 L44 44 L30 38 L18 46z" fill="#fff"/></svg>
  <h3>CRM</h3><div class="dash"></div>
  <p>Lorem ipsum dolor sit amet, consectetur adipiscing elit, s ed do eiusmod tempor</p>
  <span class="go"><svg width="14" height="14" viewBox="0 0 14 14"><path d="M1 7h11M8 3l4 4-4 4" stroke="#fff" stroke-width="1.6" fill="none"/></svg></span>
</div>

<!-- product detail band -->
<svg class="abs" style="left:0;top:1700px" width="1200" height="765" viewBox="0 0 1200 765">
  <defs><linearGradient id="band" x1="0" y1="0" x2="0" y2="1"><stop offset="0" stop-color="#0b58ad"/><stop offset="1" stop-color="#6d9fd4"/></linearGradient></defs>
  <polygon points="0,230 890,0 1200,190 1200,765 0,765" fill="url(#band)"/>
  <polygon points="125,200 890,40 1200,230 1200,190 890,0 0,230 0,232" fill="var(--blue)"/>
  <polyline points="125,200 890,40 1200,232" fill="none" stroke="#fff" stroke-width="4"/>
  <circle cx="860" cy="440" r="125" fill="rgba(202,222,239,.4)"/>
</svg>
<div class="tabs">
  <div class="tab">Nemo enim</div><div class="tab on">Nemo enim</div><div class="tab">Nemo enim</div><div class="tab">Nemo enim</div>
</div>
<h2 class="p-title">Product 1</h2>
<p class="p-text">Lorem ipsum dolor sit amet, consectetur adipiscing elit, sed do eiusmod tempor incididunt ut labore et dolore magna aliqua. Ut enim ad minim veniam, quis nostrud exercitation ullamco laboris nisi ut aliquip ex ea commodo consequat. Duis aute irure dolor in reprehenderit in voluptate velit esse cillum dolore eu fugiat nulla pariatur. Excepteur sint occaecat cupidatat non proident, sunt in culpa qui officia deserunt mollit anim id est laborum. Lorem ipsum dolor sit amet, consectetur adipiscing elit, sed do eiusmod tempor incididunt ut labore et dolore magna aliqua. Ut enim ad minim veniam, quis nostrud exercitation</p>
<div class="laptop" role="img" aria-label="Laptop showing the accounting software trial balance screen"></div>

<!-- call to action -->
<div class="cta-box"></div>
<div class="cta-person" role="img" aria-label="Photo of a smiling man in a green jacket holding a laptop"></div>
<h2 class="cta-head">What are you waiting for? Create a free account in <span>Velto.Cr?</span></h2>
<div class="btn-outline cta-btn">CREATE FREE ACCOUNT <svg width="13" height="13" viewBox="0 0 14 14"><circle cx="7" cy="7" r="7" fill="var(--blue)"/><path d="M5 3.5l3.5 3.5L5 10.5" stroke="#fff" stroke-width="2" fill="none"/></svg></div>

<!-- footer -->
<svg class="abs" style="left:0;top:2930px" width="1200" height="750" viewBox="0 0 1200 750">
  <defs><linearGradient id="foot" x1="0" y1="0" x2="0" y2="1"><stop offset="0" stop-color="#0a55aa"/><stop offset="1" stop-color="#083f8a"/></linearGradient></defs>
  <circle cx="988" cy="200" r="200" fill="rgba(202,222,239,.45)"/>
  <polygon points="0,400 310,166 1200,440 1200,750 0,750" fill="url(#foot)"/>
  <polyline points="0,420 300,262 1200,470" fill="none" stroke="#fff" stroke-width="4"/>
</svg>
<div class="footer-col" style="left:147px">
  <h4>COMPANY</h4>
  <ul><li>Home</li><li>About us</li><li>Services</li><li>News</li><li>Blog</li></ul>
</div>
<div class="footer-col" style="left:361px">
  <h4>RESOURCES</h4>
  <ul><li>Support</li><li>Testimonials</li><li>Sitemap</li><li>Career</li><li>Contact us</li></ul>
</div>
<div class="footer-col" style="left:583px;width:260px">
  <h4>CONTACT US</h4>
  <div class="contact-row"><svg width="12" height="14" viewBox="0 0 12 14"><path d="M6 0a5 5 0 0 1 5 5c0 4-5 9-5 9S1 9 1 5a5 5 0 0 1 5-5z" fill="var(--blue-3)"/><circle cx="6" cy="5" r="2" fill="#0a55aa"/></svg><span>Lorem ipsum dolor sit amet, consectetur</span></div>
  <div class="contact-row"><svg width="12" height="12" viewBox="0 0 12 12"><path d="M2 0l3 3-2 2a7 7 0 0 0 4 4l2-2 3 3-2 2C5 12 0 7 0 2z" fill="var(--blue-3)"/></svg><span>+1 555 014 2398</span></div>
  <div class="contact-row"><svg width="14" height="10" viewBox="0 0 14 10"><rect width="14" height="10" fill="var(--blue-3)"/><path d="M0 0l7 6 7-6" stroke="#0a55aa" fill="none"/></svg><span>info@veltomail.com</span></div>
</div>
<div class="foot-brand"><i></i>velto.cr</div>
<div class="slogan">WE KEEP YOU COVERED</div>
<div class="socials"><i></i><i></i><i></i><i></i></div>
<p class="copyright">© Copyrights 2022 Company name |All Rights Reserved</p>

</body>
</html>
```